Fence Flyer to Attract More Sales During Winter

We need a new flyer made that we can distribute to residential mailboxes. The flyer is to promote our Frostline Picket Days. We like simply designs, and we would like the flyer to showcase a lot of our fence photos. More of our photos are online at our website at www.getbramblerail.com - our new address needs to also be featured on the flyer - 436 Quillen rd, Monroe, NC 28117. I do want the words "FROSTLINE PICKET DAYS" to be dominate on the flyer with the description "Wood fences starting at $12/FT!" Please look through our Facebook page and our website to gather more photos or information. We are flexible on colors, nothing to fancy - simple flyer design please.

Target Market(s)

Residential homeowners that need a new fence to enclose their yard for safety, security or decorative

Industry/Entity Type

Residential Construction

Font styles to use
Sans Serif

Colors

Designer to choose colors to be used in the design.

Requirements
Must have
• Frostline Picket Days
• Contact information for the business
• "Come visit our outdoor showroom, open 24/7!"
Nice to have
• Photos of our fences - you can find more on our website at www.GetBrambleRail.com or Facebook.com/MeadowlarkRailGPV
Should not have
• Flashy designs

```html
<!DOCTYPE html>
<html lang="en">
<head>
<meta charset="utf-8">
<title>Meadowlark Rail – Frostline Picket Days Flyer</title>
<link rel="stylesheet" href="https://fonts.googleapis.com/css2?family=Anton&family=Exo+2:wght@600;700;800&family=Mulish:wght@600;700;800&display=swap">
<style>
  :root {
    --backdrop: #c9c7c3;
    --paper: #ffffff;
    --brand-blue: #2f79bf;
    --ink: #111111;
    --band-orange: #d4862a;
    --accent-orange: #e08a24;
    --post-brown: #5a3a20;
    --wood-light: #cdb58c;
    --wood-mid: #b39869;
    --siding: #dcdad6;
    --foliage: #3d5a2c;
  }
  * { box-sizing: border-box; margin: 0; padding: 0; }
  html, body { width: 1180px; height: 1200px; overflow: hidden; }
  body { background: var(--backdrop); position: relative; font-family: "Mulish", sans-serif; }

  .flyer {
    position: absolute;
    left: 190px; top: 30px;
    width: 630px; height: 898px;
    background: var(--paper);
    transform: scale(1.27);
    transform-origin: top left;
  }

  .brand-mark {
    position: absolute; left: 52px; top: 62px;
    width: 100px; height: 100px; border-radius: 50%;
    background: var(--accent-orange);
  }
  .brand-name {
    position: absolute; left: 190px; top: 56px;
    font-family: "Exo 2", sans-serif; font-weight: 700;
    font-size: 46px; line-height: 1; color: var(--brand-blue);
  }
  .brand-phone {
    position: absolute; left: 189px; top: 116px;
    font-family: "Exo 2", sans-serif; font-weight: 800;
    font-size: 44px; line-height: 1; color: var(--ink);
  }
  .brand-tagline {
    position: absolute; left: 190px; top: 172px;
    font-family: "Exo 2", sans-serif; font-weight: 700;
    font-size: 15px; color: var(--ink); letter-spacing: 0.2px;
  }

  .photo {
    position: absolute; top: 215px; height: 301px;
  }
  .photo-left {
    left: 45px; width: 261px;
    border-left: 12px solid var(--accent-orange);
    background: linear-gradient(180deg, var(--siding) 0%, var(--siding) 34%, var(--wood-light) 40%, var(--wood-mid) 92%, #a2835a 100%);
  }
  .photo-right {
    left: 317px; width: 266px;
    border-left: 10px solid var(--post-brown);
    border-right: 10px solid var(--brand-blue);
    background: linear-gradient(180deg, #6f8a55 0%, var(--foliage) 38%, #7a8a48 55%, #a68e62 80%, #8f7750 100%);
  }

  .sale-band {
    position: absolute; left: 45px; top: 526px;
    width: 538px; height: 260px;
    background: var(--band-orange);
  }
  .sale-title {
    position: absolute; left: 40px;
    font-family: "Anton", sans-serif; color: var(--ink);
    line-height: 1; text-transform: uppercase;
  }
  .sale-title-top { top: 18px; font-size: 70px; letter-spacing: 1px; }
  .sale-title-bottom { top: 104px; font-size: 70px; letter-spacing: 1.5px; }
  .sale-divider {
    position: absolute; left: 373px; top: 29px;
    width: 2px; height: 54px; background: var(--ink);
  }
  .showroom-note {
    position: absolute; left: 397px; top: 26px;
    font-family: "Mulish", sans-serif; font-weight: 700;
    font-size: 17px; line-height: 1.07; color: var(--ink);
  }
  .sale-rule {
    position: absolute; left: 40px; top: 210px;
    width: 458px; height: 2px; background: var(--ink);
  }
  .sale-offer {
    position: absolute; left: 40px; top: 216px; width: 458px;
    text-align: center;
    font-family: "Mulish", sans-serif; font-weight: 800;
    font-size: 24px; color: var(--ink);
  }

  .web-address {
    position: absolute; left: 0; top: 800px; width: 630px;
    text-align: center;
    font-family: "Exo 2", sans-serif; font-weight: 800;
    font-size: 27px; letter-spacing: 2.3px; color: var(--brand-blue);
  }
  .street-address {
    position: absolute; left: 44px; top: 834px; width: 540px;
    display: flex; align-items: center; gap: 12px;
    font-family: "Mulish", sans-serif; font-weight: 600;
    font-size: 22px; color: var(--ink); white-space: nowrap;
  }
  .street-address .rule { flex: 1; height: 2px; background: var(--ink); }
</style>
</head>
<body>
  <main class="flyer">
    <div class="brand-mark" aria-hidden="true"></div>
    <div class="brand-name">Meadowlark Rail</div>
    <div class="brand-phone">704-555-0182</div>
    <div class="brand-tagline">“Because Good Fences Make Good Neighbors”</div>

    <div class="photo photo-left" role="img" aria-label="Photo of a scalloped wooden shadowbox fence and gate beside a house with grey siding"></div>
    <div class="photo photo-right" role="img" aria-label="Photo of a split-rail fence with an arched wooden gate along a grassy yard and evergreen trees"></div>

    <section class="sale-band">
      <div class="sale-title sale-title-top">Frostline</div>
      <div class="sale-divider"></div>
      <p class="showroom-note">Come visit<br>our outdoor<br>showroom,<br>open 24/7!</p>
      <div class="sale-title sale-title-bottom">Picket Days</div>
      <div class="sale-rule"></div>
      <p class="sale-offer">Wood fences starting at $12/FT!</p>
    </section>

    <div class="web-address">WWW.GETBRAMBLERAIL.COM</div>
    <div class="street-address"><span class="rule"></span>436 Quillen rd, Monroe, NC 28117<span class="rule"></span></div>
  </main>
</body>
</html>
```